QT Community Page regarding All things QT Relay Chatbots, requires Profile and Banner images.

Hi, I have setup a QT Page for Reviews and News for all things related to Quillnet Relay Chatbots. See https://www.quillnet-example.com/relaydroidhub

I plan to post regular updates on new QT Relay Chatbots released and also on News regarding developments with Quillnet Relay and also 3rd party platforms used to build Quillnet Relay Chatbots. I am solely focussing on Quillnet Relay Chatbots.

I hope to attract a huge community of like minded people interested in discussing use cases for Chatbots and recommendations of awesome QT Relay Chatbots.

Here is a similar idea for ALL Chatbots https://www.quillnet-example.com/pg/droidrostrum

I have attached my business Logo with colours. I don't intend for there to be a direct association but could probably hint an association by matching some colours. This is not important though as there is no direct connection. It is probably more important that Quillnet Relay is the signal users will get when viewing the Page.

Target Market(s)

Quillnet / Relay Users

Industry/Entity Type

Community

Requirements
Must have
• My website will look very similar to this one. I have bought this and it is in the process of being moved to my host and url. http://mindforge-sample.net/
• the banner colour should match #0E94F9
Nice to have
• Would be nice if the font can match or be similar to the font used here http://mindforge-sample.net/

```html
<!DOCTYPE html>
<html lang="en">
<head>
<meta charset="utf-8">
<title>Chatbot News and Reviews – Banner and Profile</title>
<link rel="stylesheet" href="https://fonts.googleapis.com/css2?family=Source+Sans+3:wght@600;700&display=swap">
<style>
  :root {
    --page-bg: #ffffff;
    --frame-edge: #dddfe2;
    --banner-top: #27a7e0;
    --banner-bottom: #1e73bb;
    --network-glow: rgba(94, 230, 245, 0.32);
    --title-white: #ffffff;
    --bubble-dot-1: #0e94f9;
    --bubble-dot-2: #1a8ee6;
    --bubble-dot-3: #1d7fd0;
    --profile-frame: #ffffff;
    --profile-edge: #d9d9d9;
    --profile-inner: #f2f2f2;
    --brand-blue: #0e94f9;
    --pill-dot-1: #0e94f9;
    --pill-dot-2: #6cc5f5;
    --pill-dot-3: #cdeafc;
    --tab-text: #4b4f56;
    --tab-divider: #dddfe2;
    --tab-active: #4b67a1;
  }
  html, body {
    margin: 0;
    padding: 0;
    width: 1200px;
    height: 1200px;
    overflow: hidden;
    background: var(--page-bg);
  }
  .canvas {
    position: relative;
    width: 1200px;
    height: 1200px;
    font-family: "Source Sans 3", "Source Sans Pro", sans-serif;
  }
  .page-frame {
    position: absolute;
    left: 28px;
    top: 372px;
    width: 1141px;
    height: 481px;
    border: 1px solid var(--frame-edge);
    box-sizing: content-box;
    background: var(--page-bg);
  }
  .banner {
    position: absolute;
    left: 0;
    top: 0;
    width: 100%;
    height: 420px;
    background: linear-gradient(180deg, var(--banner-top) 0%, var(--banner-bottom) 45%, var(--banner-bottom) 100%);
    overflow: hidden;
  }
  .network-field {
    position: absolute;
    top: 0;
    height: 100%;
  }
  .network-field--left {
    left: 0;
    width: 360px;
    background: radial-gradient(ellipse at 35% 35%, var(--network-glow), rgba(94, 230, 245, 0) 70%);
  }
  .network-field--right {
    right: 0;
    width: 440px;
    background: radial-gradient(ellipse at 60% 50%, var(--network-glow), rgba(94, 230, 245, 0) 72%);
  }
  .chat-bubble {
    position: absolute;
    left: 483px;
    top: 118px;
    width: 172px;
    height: 42px;
  }
  .banner-title {
    position: absolute;
    left: 0;
    right: 0;
    top: 160px;
    margin: 0;
    text-align: center;
    color: var(--title-white);
    font-weight: 700;
    font-size: 46px;
    line-height: 1;
  }
  .tab-bar {
    position: absolute;
    left: 265px;
    top: 420px;
    height: 61px;
    display: flex;
    align-items: center;
    margin: 0;
    padding: 0;
    list-style: none;
  }
  .tab {
    position: relative;
    height: 41px;
    display: flex;
    align-items: center;
    padding: 0 23px;
    color: var(--tab-text);
    font-weight: 600;
    font-size: 19px;
    border-right: 1px solid var(--tab-divider);
  }
  .tab:first-child { padding-left: 10px; padding-right: 24px; }
  .tab:last-child { border-right: none; }
  .tab--active::after {
    content: "";
    position: absolute;
    left: 0;
    right: 0;
    bottom: -15px;
    height: 5px;
    background: var(--tab-active);
  }
  .profile-card {
    position: absolute;
    left: 49px;
    top: 606px;
    width: 227px;
    height: 227px;
    background: var(--profile-frame);
    box-shadow: 0 0 0 1px var(--profile-edge), 0 1px 3px rgba(0, 0, 0, 0.15);
  }
  .profile-inner {
    position: absolute;
    inset: 6px;
    background: radial-gradient(circle at 50% 40%, #ffffff 35%, var(--profile-inner) 100%);
    box-shadow: inset 0 0 0 1px #e3e3e3;
  }
  .profile-brand {
    position: absolute;
    left: 0;
    right: 0;
    top: 58px;
    display: flex;
    flex-direction: column;
    align-items: center;
    gap: 10px;
  }
  .brand-mark {
    width: 34px;
    height: 34px;
    border-radius: 50%;
    background: var(--brand-blue);
  }
  .brand-name {
    color: var(--brand-blue);
    font-weight: 700;
    font-size: 22px;
  }
  .typing-pill {
    position: absolute;
    left: 24px;
    bottom: 20px;
    width: 169px;
    height: 36px;
  }
</style>
</head>
<body>
<main class="canvas">
  <section class="page-frame">
    <div class="banner">
      <div class="network-field network-field--left" role="img" aria-label="Decorative network of glowing connected nodes"></div>
      <div class="network-field network-field--right" role="img" aria-label="Decorative network of glowing connected nodes"></div>

      <svg class="chat-bubble" viewBox="0 0 172 42" aria-hidden="true">
        <path d="M18 1 H155 A16 16 0 0 1 155 33 H22 L0.8 40.5 L5 27 A16 16 0 0 1 18 1 Z"
              fill="none" stroke="#ffffff" stroke-width="1.4"/>
        <circle cx="22" cy="18" r="7.5" fill="var(--bubble-dot-1)"/>
        <circle cx="51" cy="18" r="7.5" fill="var(--bubble-dot-2)"/>
        <circle cx="80" cy="18" r="7.5" fill="var(--bubble-dot-3)"/>
      </svg>

      <h1 class="banner-title">Chatbot News and Reviews</h1>
    </div>

    <ul class="tab-bar">
      <li class="tab tab--active">Timeline</li>
      <li class="tab">About</li>
      <li class="tab">Photos</li>
      <li class="tab">Likes</li>
      <li class="tab">More</li>
    </ul>
  </section>

  <section class="profile-card">
    <div class="profile-inner">
      <div class="profile-brand">
        <span class="brand-mark"></span>
        <span class="brand-name">Quillnet Relay</span>
      </div>
      <svg class="typing-pill" viewBox="0 0 169 36" aria-hidden="true">
        <rect x="0.6" y="0.6" width="167.8" height="34.8" rx="17.4" fill="#ffffff" stroke="var(--brand-blue)" stroke-width="1.2"/>
        <circle cx="20" cy="18" r="7.5" fill="var(--pill-dot-1)"/>
        <circle cx="49" cy="18" r="7.5" fill="var(--pill-dot-2)"/>
        <circle cx="78" cy="18" r="7.5" fill="var(--pill-dot-3)"/>
      </svg>
    </div>
  </section>
</main>
</body>
</html>
```